Heart Rate Game Display Graphic

We need a unique layout / info-graphic for our heart rate software to display an individuals hear rate, HR%, and other data together within a larger class of up to 40 other users. Graphics should be colorful, dynamic, and intuitive.

Target Market(s)

Group Fitness Classes

Font styles to use
Sans Serif

Colors

Designer to choose colors to be used in the design.

Requirements
Must have
• Individual Box must contain data field or graphic representation of:
• User Name
• Heart Rate %
• Points Earned / % Accuracy
Nice to have
• thinking other shape design that easily integrates with 40+ of the same shape. Looking for depth of design and or some 3d visualizations. Competing companies:
• https://www.pulsevane.org/
• https://www.trovo.com/
• https://www.kestra.com/us-en/club
• https://bravulo.com/
• https://dornaly.fit/personal-trainer/
• https://www.quelvanta.io/Solutions/Heart-Rate-Training
• http://wamble.corvinladesystems.com/
• https://pell-tander.com/explore/pell-tander-indoor-cycling-app/
Should not have
• should NOT be just be plain squares representing each client.

```html
<!DOCTYPE html>
<html lang="en">
<head>
<meta charset="utf-8">
<title>Heart Rate Game Display</title>
<link rel="stylesheet" href="https://fonts.googleapis.com/css2?family=Source+Sans+3:wght@400;600;700&display=swap">
<style>
  :root {
    --night: #000000;
    --day: #ffffff;
    --track-night: #47424f;
    --track-day: #45404c;
    --ink-night-soft: #f6dcec;
    --ink-night: #ffffff;
    --ink-day: #3a3640;
    --ember-top: #ff2e7e;
    --ember-bottom: #ffa515;
    --tide-top: #6a3cff;
    --tide-bottom: #10e0d8;
    --bloom-top: #7b2ff7;
    --bloom-bottom: #ff2a8a;
  }
  * { box-sizing: border-box; margin: 0; padding: 0; }
  html, body { width: 1200px; height: 840px; overflow: hidden; }
  body { font-family: "Source Sans 3", sans-serif; }
  .gradient-defs { position: absolute; width: 0; height: 0; }

  .board { position: relative; width: 1200px; height: 420px; }
  .board--night { background: var(--night); --track: var(--track-night); --score: var(--ink-night-soft); --name: var(--ink-night-soft); --stat: var(--ink-night); }
  .board--day { background: var(--day); --track: var(--track-day); --score: var(--ink-day); --name: var(--ink-day); --stat: var(--ink-day); }

  .player { position: absolute; top: 98px; width: 140px; height: 260px; }
  .player--one { left: 374px; }
  .player--two { left: 530px; }
  .player--three { left: 687px; }

  .gauge { position: absolute; left: 0; top: 0; width: 140px; height: 140px; }
  .gauge .track { fill: none; stroke: var(--track); stroke-width: 5; }
  .gauge .arc { fill: none; stroke-width: 5; stroke-linecap: butt; }
  .gauge .score { font-family: "Source Sans 3", sans-serif; font-size: 32px; font-weight: 400; fill: var(--score); }

  .player-name { position: absolute; left: 0; top: 160px; width: 140px; text-align: center; font-size: 21px; font-weight: 400; color: var(--name); letter-spacing: -0.2px; }

  .stats { position: absolute; left: 32px; top: 188px; height: 60px; padding-left: 13px; padding-top: 10px; list-style: none; }
  .stats::before { content: ""; position: absolute; left: 0; top: 0; width: 4px; height: 60px; border-radius: 2px; background: linear-gradient(var(--bar-top), var(--bar-bottom)); }
  .stats li { font-size: 9.5px; font-weight: 700; line-height: 12.5px; color: var(--stat); white-space: nowrap; }
  .player--one .stats { --bar-top: var(--ember-top); --bar-bottom: var(--ember-bottom); }
  .player--two .stats { --bar-top: var(--tide-top); --bar-bottom: var(--tide-bottom); }
  .player--three .stats { --bar-top: var(--bloom-top); --bar-bottom: var(--bloom-bottom); }
</style>
</head>
<body>
<svg class="gradient-defs" aria-hidden="true">
  <defs>
    <linearGradient id="ember" x1="0" y1="0" x2="0" y2="1">
      <stop offset="0" stop-color="#ff2e7e"/><stop offset="1" stop-color="#ffa515"/>
    </linearGradient>
    <linearGradient id="tide" x1="0" y1="0" x2="0" y2="1">
      <stop offset="0" stop-color="#6a3cff"/><stop offset="1" stop-color="#10e0d8"/>
    </linearGradient>
    <linearGradient id="bloom" x1="0" y1="0" x2="0" y2="1">
      <stop offset="0" stop-color="#7b2ff7"/><stop offset="1" stop-color="#ff2a8a"/>
    </linearGradient>
  </defs>
</svg>

<section class="board board--night">
  <article class="player player--one">
    <svg class="gauge" viewBox="-70 -70 140 140">
      <circle class="track" r="62"/><circle class="track" r="52"/><circle class="track" r="42"/>
      <circle class="arc" r="62" pathLength="100" stroke="url(#ember)" stroke-dasharray="36 100" transform="rotate(-219.6)"/>
      <circle class="arc" r="52" pathLength="100" stroke="url(#ember)" stroke-dasharray="68 100" transform="rotate(-334.8)"/>
      <circle class="arc" r="42" pathLength="100" stroke="url(#ember)" stroke-dasharray="72 100" transform="rotate(-349.2)"/>
      <text class="score" x="0" y="11" text-anchor="middle">25</text>
    </svg>
    <h2 class="player-name">Username</h2>
    <ul class="stats"><li>Heart Rate 10%</li><li>&nbsp;Points Earned 25</li><li>Accuracy 98%</li></ul>
  </article>
  <article class="player player--two">
    <svg class="gauge" viewBox="-70 -70 140 140">
      <circle class="track" r="62"/><circle class="track" r="52"/><circle class="track" r="42"/>
      <circle class="arc" r="62" pathLength="100" stroke="url(#tide)" stroke-dasharray="16 100" transform="rotate(-147.6)"/>
      <circle class="arc" r="52" pathLength="100" stroke="url(#tide)" stroke-dasharray="58 100" transform="rotate(-298.8)"/>
      <circle class="arc" r="42" pathLength="100" stroke="url(#tide)" stroke-dasharray="40 100" transform="rotate(-294)"/>
      <text class="score" x="0" y="11" text-anchor="middle">50</text>
    </svg>
    <h2 class="player-name">Username</h2>
    <ul class="stats"><li>Heart Rate 57%</li><li>Points Earned 50</li><li>Accuracy 34%</li></ul>
  </article>
  <article class="player player--three">
    <svg class="gauge" viewBox="-70 -70 140 140">
      <circle class="track" r="62"/><circle class="track" r="52"/><circle class="track" r="42"/>
      <circle class="arc" r="62" pathLength="100" stroke="url(#bloom)" stroke-dasharray="42 100" transform="rotate(0)"/>
      <circle class="arc" r="52" pathLength="100" stroke="url(#bloom)" stroke-dasharray="58 100" transform="rotate(-298.8)"/>
      <circle class="arc" r="42" pathLength="100" stroke="url(#bloom)" stroke-dasharray="42 100" transform="rotate(-60)"/>
      <text class="score" x="0" y="11" text-anchor="middle">75</text>
    </svg>
    <h2 class="player-name">Username</h2>
    <ul class="stats"><li>Heart Rate 74%</li><li>Points Earned 99</li><li>Accuracy 10%</li></ul>
  </article>
</section>

<section class="board board--day">
  <article class="player player--one">
    <svg class="gauge" viewBox="-70 -70 140 140">
      <circle class="track" r="62"/><circle class="track" r="52"/><circle class="track" r="42"/>
      <circle class="arc" r="62" pathLength="100" stroke="url(#ember)" stroke-dasharray="36 100" transform="rotate(-219.6)"/>
      <circle class="arc" r="52" pathLength="100" stroke="url(#ember)" stroke-dasharray="68 100" transform="rotate(-334.8)"/>
      <circle class="arc" r="42" pathLength="100" stroke="url(#ember)" stroke-dasharray="72 100" transform="rotate(-349.2)"/>
      <text class="score" x="0" y="11" text-anchor="middle">25</text>
    </svg>
    <h2 class="player-name">Username</h2>
    <ul class="stats"><li>Heart Rate 10%</li><li>&nbsp;Points Earned 25</li><li>Accuracy 98%</li></ul>
  </article>
  <article class="player player--two">
    <svg class="gauge" viewBox="-70 -70 140 140">
      <circle class="track" r="62"/><circle class="track" r="52"/><circle class="track" r="42"/>
      <circle class="arc" r="62" pathLength="100" stroke="url(#tide)" stroke-dasharray="16 100" transform="rotate(-147.6)"/>
      <circle class="arc" r="52" pathLength="100" stroke="url(#tide)" stroke-dasharray="58 100" transform="rotate(-298.8)"/>
      <circle class="arc" r="42" pathLength="100" stroke="url(#tide)" stroke-dasharray="40 100" transform="rotate(-294)"/>
      <text class="score" x="0" y="11" text-anchor="middle">50</text>
    </svg>
    <h2 class="player-name">Username</h2>
    <ul class="stats"><li>Heart Rate 57%</li><li>Points Earned 50</li><li>Accuracy 34%</li></ul>
  </article>
  <article class="player player--three">
    <svg class="gauge" viewBox="-70 -70 140 140">
      <circle class="track" r="62"/><circle class="track" r="52"/><circle class="track" r="42"/>
      <circle class="arc" r="62" pathLength="100" stroke="url(#bloom)" stroke-dasharray="42 100" transform="rotate(0)"/>
      <circle class="arc" r="52" pathLength="100" stroke="url(#bloom)" stroke-dasharray="58 100" transform="rotate(-298.8)"/>
      <circle class="arc" r="42" pathLength="100" stroke="url(#bloom)" stroke-dasharray="42 100" transform="rotate(-60)"/>
      <text class="score" x="0" y="11" text-anchor="middle">75</text>
    </svg>
    <h2 class="player-name">Username</h2>
    <ul class="stats"><li>Heart Rate 74%</li><li>Points Earned 99</li><li>Accuracy 10%</li></ul>
  </article>
</section>
</body>
</html>
```